DeskWizard.dk Frontpage design

I'm in the process of starting a It-course website, based in Denmark. The web site Url is - www.deskwizard.dk

The services are:
- Online courses (This is the main service and the most important)
- One to One courses
- Webinar

I need a frontpage design a simple design, but it must shows professionalism. I have no preference in color, but I like white space.

In Denmark the established competitors are:
- www.tasniva.dk (Biggest competitor)
- www.bramfeldt.dk/online-kurser
- www.velunda.dk

Target Market(s)

Mainly companies (B to B), but there are also a small number of private customers

Industry/Entity Type

Online it courses and one to one consulting

Number of Pages Required

1 page

Font styles to use
Sans Serif

Requirements
Must have
• A professional design, white space

```html
<!DOCTYPE html>
<html lang="en">
<head>
<meta charset="utf-8">
<title>DeskWizard.dk – Online IT courses</title>
<link href="https://fonts.googleapis.com/css2?family=Poppins:wght@400;500;600;700&family=Roboto:ital,wght@0,300;0,400;1,300&display=swap" rel="stylesheet">
<style>
:root{
  --orange:#ff6a00;
  --orange-soft:#fde9dc;
  --ink:#333333;
  --ink-soft:#6b6b6b;
  --line:#e6e6e6;
  --band:#f4f7fd;
  --peach:#fdf5ef;
  --icon-dark:#4a4a4a;
  --footer:#121212;
  --white:#ffffff;
}
*{box-sizing:border-box;margin:0;padding:0}
html,body{width:1200px;height:3546px;overflow:hidden}
body{position:relative;background:var(--white);font-family:'Poppins',sans-serif;color:var(--ink)}
.abs{position:absolute}
a{color:inherit;text-decoration:none}

/* hero */
.hero{position:absolute;left:0;top:0;width:1200px;height:615px;
  background:linear-gradient(115deg,#2a2520 0%,#3b342b 30%,#2c4a4e 60%,#6b5a45 85%,#8a7355 100%)}
.hero-shade{position:absolute;inset:0;background:linear-gradient(90deg,rgba(0,0,0,.45) 0%,rgba(0,0,0,.1) 60%,rgba(0,0,0,0) 100%)}
.brand{font-family:'Poppins',sans-serif;font-weight:600;font-size:29px;color:var(--white)}
.nav{position:absolute;left:527px;top:26px;display:flex;gap:17px;font-size:11px;font-weight:500;color:var(--white)}
.btn{display:inline-flex;align-items:center;justify-content:center;gap:5px;border-radius:16px;
  font-family:'Poppins',sans-serif;font-weight:600;font-size:9.5px;text-transform:uppercase;color:var(--white);background:var(--orange)}
.btn-ghost{background:transparent;border:2px solid var(--white)}
.hero h1{position:absolute;left:183px;top:178px;width:400px;font-size:45px;line-height:49px;font-weight:600;color:var(--white)}
.hero-lead{position:absolute;left:183px;top:382px;font-family:'Roboto',sans-serif;font-size:11px;line-height:16px;color:var(--white)}
.notch{position:absolute;left:570px;top:600px;width:60px;height:30px;border-radius:30px 30px 0 0;background:var(--white)}

/* section heads */
.sec-title{position:absolute;left:0;width:1200px;text-align:center;font-weight:700;font-size:41px;color:var(--ink)}
.sec-sub{position:absolute;left:0;width:1200px;text-align:center;font-family:'Roboto',sans-serif;font-size:16px;color:var(--ink)}

/* course cards */
.course{position:absolute;top:791px;width:267px;height:321px;background:var(--white);border:1px solid var(--line);border-radius:4px}
.course.featured{border-color:transparent;box-shadow:0 25px 60px rgba(0,0,0,.08)}
.price{position:absolute;left:22px;top:18px;font-size:12px;font-weight:600;color:var(--orange)}
.course-mark{position:absolute;left:50%;top:30px;width:80px;height:80px;margin-left:-40px;border-radius:14px}
.course h3{position:absolute;left:0;width:100%;top:125px;text-align:center;font-weight:500;font-size:21px;line-height:26px}
.course p{position:absolute;left:24px;right:24px;text-align:center;font-family:'Roboto',sans-serif;font-size:11px;line-height:17px;color:var(--ink-soft)}
.tags{position:absolute;left:14px;top:280px;display:flex;gap:6px}
.tag{background:var(--orange-soft);color:var(--orange);font-size:8.5px;font-weight:600;padding:3px 12px;border-radius:10px}
.arrow{position:absolute;right:22px;top:282px}

/* features */
.feature{position:absolute;top:1360px;width:230px;text-align:center}
.feature-ring{width:122px;height:122px;margin:0 auto;border:1.5px dashed #555;border-radius:50%;padding:5px}
.feature-ring .disc{width:100%;height:100%;border-radius:50%;background:var(--icon-dark);display:flex;align-items:center;justify-content:center}
.feature.active .feature-ring{border-color:var(--orange)}
.feature.active .disc{background:var(--orange)}
.feature h4{margin-top:14px;font-weight:500;font-size:19px}
.feature p{margin-top:4px;font-family:'Roboto',sans-serif;font-size:11px;line-height:17px;color:var(--ink-soft)}

/* webinar */
.band{position:absolute;left:0;top:1658px;width:1200px;height:702px;background:var(--band)}
.italic-note{position:absolute;left:0;width:1200px;text-align:center;font-family:'Roboto',sans-serif;font-style:italic;font-weight:300;font-size:13.5px;line-height:17px;color:var(--ink)}
.video{position:absolute;left:253px;top:1885px;width:697px;height:352px;
  background:linear-gradient(100deg,#c9c3b4 0%,#5b5647 22%,#2a2824 45%,#3d3a33 70%,#7b6c55 100%)}
.play{position:absolute;left:301px;top:129px;width:94px;height:94px;border:2.5px solid var(--white);border-radius:50%}

/* blog */
.post{position:absolute;top:2525px;width:400px;height:220px;border:1px solid var(--line);border-radius:3px;background:var(--white)}
.post-mark{position:absolute;border-radius:8px}
.post-body{position:absolute;right:18px}
.meta{font-size:9.5px;color:var(--ink)}
.post h5{margin-top:8px;font-weight:500;font-size:13px;color:#1f2d4a}
.post p{margin-top:4px;font-size:12px;line-height:15.5px;color:var(--ink)}
.read{display:inline-block;margin-top:8px;font-size:8px;color:var(--orange);text-decoration:underline}

/* one to one */
.one h2{position:absolute;left:664px;top:2986px;font-weight:600;font-size:41px}
.one p{position:absolute;left:665px;top:3053px;width:340px;font-size:17.5px;line-height:27px;color:var(--ink)}

/* footer */
.footer{position:absolute;left:0;top:3353px;width:1200px;height:193px;background:var(--footer);color:var(--white);text-align:center}
.footer .brand{position:absolute;left:0;width:1200px;top:34px;font-size:27px}
.foot-nav{position:absolute;left:0;width:1200px;top:86px;display:flex;justify-content:center;gap:16px;font-size:9.5px}
.social{position:absolute;left:0;width:1200px;top:117px;display:flex;justify-content:center;gap:8px}
.social i{display:block;width:10px;height:10px;border-radius:50%;background:var(--white)}
.copy{position:absolute;left:0;width:1200px;top:140px;font-size:7px}
</style>
</head>
<body>

<!-- Hero -->
<header class="hero" role="img" aria-label="Photo of smiling colleagues working together at a laptop in a warm office">
  <div class="hero-shade"></div>
  <div class="brand abs" style="left:172px;top:15px">DeskWizard</div>
  <nav class="nav">
    <a>Courses</a><a>Webinar</a><a>One to one</a><a>Questions</a><a>Blog</a><a>About</a><a>Contact</a>
  </nav>
  <a class="btn abs" style="left:947px;top:24px;width:80px;height:23px">Sign in
    <svg width="9" height="9" viewBox="0 0 10 10"><path d="M1 5h7M5 2l3 3-3 3" stroke="#fff" stroke-width="1.6" fill="none"/></svg></a>
  <h1>Strengthen your IT skills with "just-in-time" learning</h1>
  <p class="hero-lead">I offer online courses and webinars with a clear focus,<br>or what about online "One to One" teaching</p>
  <svg class="abs" style="left:395px;top:400px" width="70" height="60" viewBox="0 0 70 60"><path d="M62 2C60 30 40 48 6 52M6 52l9-7M6 52l10 4" stroke="#fff" stroke-width="1.6" fill="none"/></svg>
  <a class="btn abs" style="left:183px;top:443px;width:100px;height:29px">Get started</a>
  <a class="btn btn-ghost abs" style="left:293px;top:443px;width:92px;height:29px">
    <svg width="9" height="10" viewBox="0 0 9 10"><path d="M1 1l7 4-7 4z" fill="#fff"/></svg>Be video</a>
  <div class="notch"></div>
  <svg class="abs" style="left:594px;top:609px" width="12" height="8" viewBox="0 0 12 8"><path d="M1 1l5 5 5-5" stroke="#333" stroke-width="1.6" fill="none"/></svg>
</header>

<!-- Selected courses -->
<h2 class="sec-title" style="top:656px">Selected Courses</h2>
<p class="sec-sub" style="top:710px">Find your next online course here</p>

<article class="course featured" style="left:175px">
  <span class="price">199 kr.</span>
  <div class="course-mark" style="background:#f2c811"></div>
  <h3>Lumetra Insight<br>in one hour</h3>
  <p style="top:188px">Is it possible to learn Lumetra Insight in just one hour? Probably not, but I can give you an introduction.</p>
  <div class="tags"><span class="tag">INSIGHT</span></div>
  <svg class="arrow" width="18" height="14" viewBox="0 0 18 14"><path d="M1 7h15M10 1l6 6-6 6" stroke="#ff6a00" stroke-width="1.8" fill="none"/></svg>
</article>

<article class="course" style="left:464px">
  <span class="price">499 kr.</span>
  <div class="course-mark" style="background:#3f78b0"></div>
  <h3>Pyra for<br>Sheetly users</h3>
  <p style="top:188px">How do you as Sheetly users get started using Pyra</p>
  <div class="tags"><span class="tag">PYRA</span><span class="tag">SHEETLY</span></div>
  <svg class="arrow" width="18" height="14" viewBox="0 0 18 14"><path d="M1 7h15M10 1l6 6-6 6" stroke="#ff6a00" stroke-width="1.8" fill="none"/></svg>
</article>

<article class="course" style="left:758px">
  <span class="price">499 kr.</span>
  <div class="course-mark" style="background:#2266b8;border-radius:50%"></div>
  <h3 style="top:140px">Statcore Introduction</h3>
  <p style="top:174px">Introduction to Statcore programming.</p>
  <div class="tags"><span class="tag">PYRA</span></div>
  <svg class="arrow" width="18" height="14" viewBox="0 0 18 14"><path d="M1 7h15M10 1l6 6-6 6" stroke="#ff6a00" stroke-width="1.8" fill="none"/></svg>
</article>

<!-- Why -->
<h2 class="sec-title" style="top:1219px">Why DeskWizard?</h2>
<p class="sec-sub" style="top:1278px">I have been teaching a lot of happy students since 1995.</p>

<div class="feature active" style="left:152px">
  <div class="feature-ring"><div class="disc">
    <svg width="56" height="56" viewBox="0 0 56 56" fill="none" stroke="#fff" stroke-width="2"><circle cx="28" cy="20" r="11"/><path d="M28 13v14M24 17h6a2 2 0 010 4h-4a2 2 0 000 4h6"/><path d="M8 30l8 14h10M48 30l-8 14H30"/></svg>
  </div></div>
  <h4>Good economy</h4>
  <p>The price of an online course is lower<br>than a physical course</p>
</div>
<div class="feature" style="left:362px">
  <div class="feature-ring"><div class="disc">
    <svg width="56" height="56" viewBox="0 0 56 56" fill="none" stroke="#fff" stroke-width="2"><circle cx="28" cy="28" r="18"/><path d="M20 18h16M20 38h16M22 18l12 20M34 18L22 38"/></svg>
  </div></div>
  <h4>Why wait</h4>
  <p>Strengthen your skills on an<br>online course now</p>
</div>
<div class="feature" style="left:563px">
  <div class="feature-ring"><div class="disc">
    <svg width="56" height="56" viewBox="0 0 56 56" fill="none" stroke="#fff" stroke-width="2"><circle cx="28" cy="30" r="17"/><circle cx="28" cy="30" r="11"/><path d="M28 30l5-5M24 9h8M28 9v4"/></svg>
  </div></div>
  <h4>No travel time</h4>
  <p>You avoid wasted time and decide for<br>yourself what to have for lunch</p>
</div>
<div class="feature" style="left:786px">
  <div class="feature-ring"><div class="disc">
    <svg width="56" height="56" viewBox="0 0 56 56" fill="none" stroke="#fff" stroke-width="2"><rect x="8" y="12" width="38" height="28" rx="3"/><path d="M8 19h38"/><circle cx="40" cy="40" r="8"/><path d="M40 36v8M36 40h8"/></svg>
  </div></div>
  <h4>Designed in a browser</h4>
  <p>Designing in a browser allows rapid<br>development and saves cost.</p>
</div>

<!-- Webinar -->
<section class="band"></section>
<h2 class="sec-title" style="top:1694px">Webinar</h2>
<p class="sec-sub" style="top:1754px">It is not only on the price that webinars beat traditional courses!</p>
<p class="italic-note" style="top:1789px">You get the same high quality in a webinar as in a traditional course, even with the advantage<br>that you can watch them again and again.</p>
<p class="italic-note" style="top:1840px">Best of all, you do not have to move to gain new knowledge</p>
<div class="video" role="img" aria-label="Photo of a person working at a desk with monitors in a dim home office">
  <div class="play"></div>
  <svg class="abs" style="left:335px;top:163px" width="30" height="28" viewBox="0 0 30 28"><path d="M2 2l26 12L2 26z" fill="#ff6a00"/></svg>
</div>
<a class="btn abs" style="left:542px;top:2272px;width:99px;height:29px">Webinar</a>

<!-- Blog -->
<h2 class="sec-title" style="top:2427px">Latest Blog Posts</h2>
<article class="post" style="left:190px">
  <div class="post-mark" style="left:16px;top:28px;width:166px;height:150px;background:#1f8a4c"></div>
  <div class="post-body" style="left:213px;top:56px">
    <div class="meta">Sheetly &bull; July 04, 2022</div>
    <h5>Current sum</h5>
    <p>Creation of current totals</p>
    <a class="read">Read the article</a>
  </div>
</article>
<article class="post" style="left:618px">
  <div class="post-mark" style="left:14px;top:28px;width:117px;height:158px;background:#e9b714"></div>
  <div class="post-body" style="left:150px;top:46px">
    <div class="meta">Insight &nbsp; sheetly &bull; June 17, 2022</div>
    <h5>Brug Insight data i Sheetly</h5>
    <p>Lumetra Insight is a great program for analyzing, viewing and sharing your report – But what if you want to analyze further on data in Sheetly?</p>
    <a class="read">Read the article</a>
  </div>
</article>

<!-- One to one -->
<svg class="abs" style="left:0;top:2815px" width="1200" height="540" viewBox="0 0 1200 540" preserveAspectRatio="none">
  <path d="M0 150C150 60 320 20 520 40C760 60 860 130 1200 100V540H0Z" fill="var(--peach)"/>
</svg>
<svg class="abs" style="left:206px;top:2883px" width="400" height="392" viewBox="0 0 400 392" role="img" aria-label="Photo of two smiling colleagues looking at a tablet together">
  <defs><linearGradient id="pairTones" x1="0" y1="0" x2="1" y2="1"><stop offset="0" stop-color="#d7a25c"/><stop offset=".5" stop-color="#8a6a4e"/><stop offset="1" stop-color="#5c84a8"/></linearGradient></defs>
  <path d="M40 130C70 60 150 75 200 30C260-15 360 10 390 90C410 160 380 250 320 320C260 390 130 400 60 350C0 300 10 200 40 130Z" fill="url(#pairTones)"/>
</svg>
<section class="one">
  <h2>One to one</h2>
  <p>Targeted teaching at just the right time will make you better and faster for your assignments</p>
</section>
<a class="btn abs" style="left:666px;top:3165px;width:118px;height:28px">One to one</a>

<!-- Footer -->
<footer class="footer">
  <div class="brand">DeskWizard</div>
  <nav class="foot-nav">
    <a>Courses</a><a>Webinar</a><a>One to one</a><a>Questions</a><a>Blog</a><a>About</a><a>Contact</a><a>Terms</a>
  </nav>
  <div class="social"><i></i><i></i><i></i></div>
  <p class="copy">Copyright © 2022 DeskWizard All Rights Reserved</p>
</footer>

</body>
</html>
```